Need simple and modern looking business card with all my information on one side and logo on the other side
Info :
Company name - VELMAR CONSTRUCTION LLC
Company addres- 418 harbor 87th. Dunmoor park ny 10352
Email- velmarllc@tridomail.Com
Company phone number 555-318-6094
Cell number- 555-742-0583
Web site - velmarllc.Com
My name Gerald tomasino

Target Market(s)

Construction , home improvement, remodeling

Industry/Entity Type

Construction

Contact Information for Business Card

It has to be moder but at the same time simple

Font styles to use
Sans Serif

Colors
0255a3
ffffff
000000
f78f20
b1b1b1
9d9d9d
1b1b1b
33a6d7
ec1f27

Requirements
Must have
• My logo on one side maybe with a some kind of background on the other side all my information
Nice to have
• Some kind of background pictures provided by you .PLEASE HAVE ACCOUNT WITH PIXELVAULT WILL NOT PAY ANY EXTRA FEES .
Should not have
• Any kind of hamer, nails,screws, helmets itp. Please do not copy the other designs come up with something new.

```html
<!DOCTYPE html>
<html lang="en">
<head>
<meta charset="utf-8">
<title>Velmar Construction LLC – Business Card Front</title>
<link rel="stylesheet" href="https://fonts.googleapis.com/css2?family=Michroma&display=swap">
<style>
  :root {
    --stage: #f1f1f1;
    --paper: #ffffff;
    --ink: #1b1b1b;
    --accent-orange: #f78f20;
    --sky-top: #2f2f9e;
    --sky-mid: #3d4fb8;
    --city-dark: #1a2450;
    --city-lights: #c9a04c;
    --water: #1f5c70;
    --edge-shadow: #b1b1b1;
  }
  html, body {
    margin: 0;
    width: 1200px;
    height: 1000px;
    overflow: hidden;
    background: var(--stage);
  }
  .card {
    position: absolute;
    left: 75px;
    top: 200px;
    width: 1050px;
    height: 600px;
    background: var(--paper);
    box-shadow: 0 6px 24px rgba(0,0,0,0.18);
    overflow: hidden;
  }
  .card__photo {
    position: absolute;
    inset: 0;
    width: 1050px;
    height: 600px;
  }
  .brand {
    position: absolute;
    right: 70px;
    bottom: 70px;
    font-family: "Michroma", sans-serif;
    color: var(--ink);
    font-weight: 400;
    text-align: right;
  }
  .brand__row {
    display: flex;
    align-items: center;
    justify-content: flex-end;
    gap: 22px;
  }
  .brand__mark {
    width: 46px;
    height: 46px;
    background: var(--accent-orange);
  }
  .brand__name {
    font-size: 104px;
    line-height: 1;
    letter-spacing: 2px;
  }
  .brand__sub {
    margin-top: 14px;
    font-size: 38px;
    line-height: 1;
    letter-spacing: 3px;
  }
</style>
</head>
<body>
  <main class="card">
    <svg class="card__photo" viewBox="0 0 1050 600" xmlns="http://www.w3.org/2000/svg">
      <defs>
        <linearGradient id="night-city" x1="0" y1="0" x2="0" y2="1">
          <stop offset="0" stop-color="var(--sky-top)"/>
          <stop offset="0.3" stop-color="var(--sky-mid)"/>
          <stop offset="0.48" stop-color="var(--city-dark)"/>
          <stop offset="0.62" stop-color="var(--city-lights)"/>
          <stop offset="0.68" stop-color="var(--city-dark)"/>
          <stop offset="1" stop-color="var(--water)"/>
        </linearGradient>
      </defs>
      <g role="img" aria-label="Night skyline photograph of tall city towers with lit windows reflected in the water">
        <polygon fill="url(#night-city)"
          points="0,0 1050,0 1050,140 1010,150 975,148 940,168 900,172 860,190 830,196 790,214 750,222 715,240 680,244 640,262 600,268 560,288 520,294 480,312 445,318 405,338 365,344 330,362 290,370 250,388 215,394 175,414 140,420 100,438 60,446 25,462 0,466"/>
      </g>
      <polyline fill="none" stroke="var(--edge-shadow)" stroke-width="2" opacity="0.6"
        points="1050,146 1010,156 975,154 940,174 900,178 860,196 830,202 790,220 750,228 715,246 680,250 640,268 600,274 560,294 520,300 480,318 445,324 405,344 365,350 330,368 290,376 250,394 215,400 175,420 140,426 100,444 60,452 25,468 0,472"/>
    </svg>

    <div class="brand">
      <div class="brand__row">
        <span class="brand__mark"></span>
        <span class="brand__name">VELMAR</span>
      </div>
      <div class="brand__sub">CONSTRUCTION LLC</div>
    </div>
  </main>
</body>
</html>
```